Law Office needs stationery design and business card

I currently have been using the same letterhead for the last 8 years. Since i 'm about to adding another location, I want to revamp my letterhead and business card. I already have a logo i'm happy with. I will upload my current letterhead, fax sheet, envelope, and logos. I need a business card also. I have 2 locations, 1 phone number, 1 fax line, website, etc. If possible and fitting with the design, I would like to keep the same information listed currently on the letterhead.

**Keep in mind, I also NEED A FAX SHEET COVER. thank you
Updates

Hello, Please submit a Gray Scale or Black and White version of your designs also, since most of the time I will be printing NON color stationery. I will seldom use a color print for my letterhead, I would like to have a color version for my benefit, however i will print in grayscale majority of the time . For the Business Card, that can just be in color. When I get my business cards they will be in color.Thank youEnrique Added Sunday, September 18, 2016

Industry/Entity Type

Business

```html
<!DOCTYPE html>
<html lang="en">
<head>
<meta charset="utf-8">
<title>Marlowe Law – Business Card</title>
<link rel="stylesheet" href="https://fonts.googleapis.com/css2?family=Cormorant+Garamond:wght@500&family=Courgette&family=Didact+Gothic&display=swap">
<style>
  :root {
    --paper: #ffffff;
    --gold: #b39a63;
    --name-grey: #6d6d6d;
    --text-grey: #4f4f4f;
  }
  * { margin: 0; padding: 0; box-sizing: border-box; }
  html, body {
    width: 1200px;
    height: 667px;
    overflow: hidden;
    background: var(--paper);
  }
  .card {
    position: relative;
    width: 1200px;
    height: 667px;
    background: var(--paper);
  }
  .brand-mark {
    position: absolute;
    left: 532px;
    top: 100px;
    width: 136px;
    height: 136px;
    background: var(--gold);
  }
  .firm-name {
    position: absolute;
    left: 0;
    width: 100%;
    top: 282px;
    text-align: center;
    font-family: "Cormorant Garamond", Georgia, serif;
    font-weight: 500;
    font-size: 58px;
    letter-spacing: 1px;
    color: var(--gold);
    line-height: 1;
  }
  .attorney-name {
    position: absolute;
    left: 0;
    width: 100%;
    top: 398px;
    text-align: center;
    font-family: "Courgette", cursive;
    font-size: 46px;
    color: var(--name-grey);
    letter-spacing: 1px;
    line-height: 1;
  }
  .divider {
    position: absolute;
    left: 146px;
    top: 488px;
    width: 912px;
    height: 20px;
  }
  .contact {
    position: absolute;
    left: 0;
    width: 100%;
    top: 526px;
    text-align: center;
    font-family: "Didact Gothic", "Century Gothic", sans-serif;
    font-size: 32px;
    letter-spacing: 1.5px;
    color: var(--text-grey);
    line-height: 47px;
  }
</style>
</head>
<body>
  <main class="card">
    <div class="brand-mark" aria-hidden="true"></div>
    <h1 class="firm-name">MARLOWE LAW</h1>
    <p class="attorney-name">Tobias Marlowe Esq</p>
    <svg class="divider" viewBox="0 0 912 20" aria-hidden="true">
      <line x1="8" y1="10" x2="904" y2="10" stroke="var(--gold)" stroke-width="3"/>
      <circle cx="8" cy="10" r="7" fill="var(--gold)"/>
      <circle cx="904" cy="10" r="7" fill="var(--gold)"/>
    </svg>
    <address class="contact" style="font-style: normal;">
      <span class="street">418 North Orange St.,Suite 200</span><br>
      <span class="city-phone">Linden, PA 19087,(610)555.0182</span>
    </address>
  </main>
</body>
</html>
```